Urine collection cup with and without sterile seal sticker

Hello. We need a urine cup label designed please with

Name:
Date of Birth:
Date:
Time:
Temp℃:
Specimen ID:

Product code: TUB-47
Volume markings (e.g., 30 mL, 60 mL, 90 mL).
Vela Drug Tests logo

Could you please provide one version with the additional sterile sticker extending to the top, and one version without the additional sterile sticker?

```html
<!DOCTYPE html>
<html lang="en">
<head>
<meta charset="utf-8">
<title>TUB-47 Urine Collection Cup Label</title>
<link href="https://fonts.googleapis.com/css2?family=Roboto:ital,wght@0,400;0,500;0,700;1,400&display=swap" rel="stylesheet">
<style>
  :root {
    --navy: #14324d;
    --blue: #1273b8;
    --bright-blue: #2a9ee0;
    --band: #e8f5fb;
    --frame: #bccbd6;
    --line: #8fa7b8;
    --muted: #5b6f80;
    --white: #ffffff;
  }
  * { box-sizing: border-box; margin: 0; padding: 0; }
  html, body { width: 1200px; height: 431px; overflow: hidden; background: var(--white); }
  body { position: relative; font-family: "Roboto", Arial, sans-serif; color: var(--navy); }

  .heading { position: absolute; top: 66px; font-size: 17px; font-weight: 700; color: #000; text-align: center; width: 400px; }
  .heading--left { left: 103px; }
  .heading--right { left: 682px; }

  .seal-tab {
    position: absolute; left: 475px; top: 27px; width: 90px; height: 114px;
    border: 4px solid var(--frame); border-bottom: none; border-radius: 12px 12px 0 0;
    background: var(--band); overflow: hidden; text-align: center;
  }
  .seal-tab__head { background: var(--blue); color: var(--white); font-weight: 700; font-size: 17px; line-height: 18px; height: 54px; padding-top: 9px; border-radius: 8px 8px 0 0; }
  .seal-tab__warn { font-size: 11.5px; font-weight: 700; line-height: 13px; padding-top: 10px; }

  .label {
    position: absolute; top: 135px; width: 520px; height: 272px;
    border: 4px solid var(--frame); border-radius: 18px; background: var(--white); overflow: hidden;
  }
  .label--seal { left: 66px; }
  .label--plain { left: 623px; }

  .label__band { position: absolute; left: 0; top: 0; right: 0; height: 54px; background: var(--band); }
  .brand { position: absolute; left: 18px; top: 6px; display: flex; align-items: center; gap: 8px; }
  .brand__dot { width: 42px; height: 42px; border-radius: 50%; background: var(--bright-blue); border: 2px solid var(--white); }
  .brand__name { font-size: 13px; font-weight: 700; color: var(--navy); }
  .product { position: absolute; left: 338px; top: 2px; }
  .product__code { font-size: 25px; font-weight: 700; line-height: 30px; }
  .product__desc { font-size: 13px; font-weight: 700; color: var(--blue); line-height: 16px; }

  .specimen {
    position: absolute; left: 16px; top: 71px; width: 480px; height: 46px;
    border: 1.5px solid var(--frame); border-radius: 7px;
  }
  .specimen__label { position: absolute; left: 10px; top: 10px; font-size: 19px; font-weight: 700; }
  .specimen__area { position: absolute; left: 325px; top: 15px; font-size: 13px; font-style: italic; color: var(--muted); }

  .field { position: absolute; display: flex; align-items: flex-end; font-size: 15px; font-weight: 700; }
  .field__line { display: block; height: 0; border-bottom: 1.5px solid var(--line); margin-left: 5px; margin-bottom: 2px; }

  .notice {
    position: absolute; left: 16px; top: 212px; width: 301px; height: 42px;
    border: 1.5px solid var(--frame); border-radius: 7px; padding: 3px 0 0 9px;
  }
  .notice__title { font-size: 15px; font-weight: 700; line-height: 17px; }
  .notice__note { font-size: 11px; font-style: italic; color: var(--muted); line-height: 16px; }

  .volume {
    position: absolute; left: 421px; top: 209px; width: 70px; height: 48px;
    border: 1.5px solid var(--frame); border-radius: 5px; padding: 1px 0 0 8px;
  }
  .volume__title { font-size: 11px; font-weight: 700; line-height: 11px; }
  .volume__option { display: flex; align-items: center; gap: 5px; font-size: 10px; line-height: 11px; }
  .volume__box { width: 8px; height: 8px; border: 1px solid var(--line); }
</style>
</head>
<body>
  <h1 class="heading heading--left">Urine Collection Cup Label</h1>
  <h1 class="heading heading--right">With &amp; Without Sterile Seal Sticker</h1>

  <div class="seal-tab">
    <div class="seal-tab__head">STERILE<br>SEAL</div>
    <div class="seal-tab__warn">DO NOT USE<br>IF BROKEN</div>
  </div>

  <section class="label label--seal">
    <div class="label__band"></div>
    <div class="brand"><span class="brand__dot"></span><span class="brand__name">Vela Drug Tests</span></div>
    <div class="product"><div class="product__code">TUB-47</div><div class="product__desc">90 mL COLLECTION CUP</div></div>
    <div class="specimen"><span class="specimen__label">Specimen ID:</span><span class="specimen__area">ID / BARCODE AREA</span></div>
    <div class="field" style="left:23px;top:136px">Name:<span class="field__line" style="width:190px"></span></div>
    <div class="field" style="left:299px;top:136px">Date of Birth:<span class="field__line" style="width:83px"></span></div>
    <div class="field" style="left:23px;top:178px">Date:<span class="field__line" style="width:85px"></span></div>
    <div class="field" style="left:196px;top:178px">Time:<span class="field__line" style="width:76px"></span></div>
    <div class="field" style="left:337px;top:178px">Temp℃:<span class="field__line" style="width:83px"></span></div>
    <div class="notice"><div class="notice__title">For single-use specimen collection</div><div class="notice__note">Verify label details before sealing / transport.</div></div>
    <div class="volume">
      <div class="volume__title">VOLUME</div>
      <div class="volume__option"><span class="volume__box"></span>90 mL</div>
      <div class="volume__option"><span class="volume__box"></span>60 mL</div>
      <div class="volume__option"><span class="volume__box"></span>30 mL</div>
    </div>
  </section>

  <section class="label label--plain">
    <div class="label__band"></div>
    <div class="brand"><span class="brand__dot"></span><span class="brand__name">Vela Drug Tests</span></div>
    <div class="product"><div class="product__code">TUB-47</div><div class="product__desc">90 mL COLLECTION CUP</div></div>
    <div class="specimen"><span class="specimen__label">Specimen ID:</span><span class="specimen__area">ID / BARCODE AREA</span></div>
    <div class="field" style="left:23px;top:136px">Name:<span class="field__line" style="width:190px"></span></div>
    <div class="field" style="left:299px;top:136px">Date of Birth:<span class="field__line" style="width:83px"></span></div>
    <div class="field" style="left:23px;top:178px">Date:<span class="field__line" style="width:85px"></span></div>
    <div class="field" style="left:196px;top:178px">Time:<span class="field__line" style="width:76px"></span></div>
    <div class="field" style="left:337px;top:178px">Temp℃:<span class="field__line" style="width:83px"></span></div>
    <div class="notice"><div class="notice__title">For single-use specimen collection</div><div class="notice__note">Verify label details before sealing / transport.</div></div>
    <div class="volume">
      <div class="volume__title">VOLUME</div>
      <div class="volume__option"><span class="volume__box"></span>90 mL</div>
      <div class="volume__option"><span class="volume__box"></span>60 mL</div>
      <div class="volume__option"><span class="volume__box"></span>30 mL</div>
    </div>
  </section>
</body>
</html>
```